Webbanner-Design für Slideshow
Zielgruppe
Annegret bietet 3 Kurse an:
diese Kurse verhelfen einem selbst seine Schutzengel wieder zu hören,
mit ihnen ihren Seelenplan weshalb man auf Erden ist zu sehen,
sowie professionell umzusetzen.
Zielgruppe:
Spirituelle Menschen,
welche Engel lieben,
an sich mental gerne in Kursen & Privat arbeiten,
neues Wissen sich liebend gerne aneignen,
ihren Seelenplan wissen und umsetzen möchten,
die Schönheit im Inneren (Seele) und
im Aussen (Körper & Umgebung) lieben.
Aufgabenstellung
Produktbannerbild für meine Website (Slideshow):
Hintergrund: vorhanden in Form von einem Jpeg, hier auf diesem Foto bitte dich einfach mit folgendem beschäftigen:
Schriftzug groß: Engel (wieder) hören lernen & deinen Seelenplan umsetzen
mit Annegret Holzmeier (klein, oder großer Schriftzug?)
Schriftzug klein: mehr …
Schriftfarbe: weiss
Schriftart: moderne Schrift (z.Bsp. was die Zeitschriften benützen)
Haus Button Schriftzug: KURSE IN MUC
Buttons Ideen, Vierecke oder Kreise ect.: Transparent bitte und in passender Farbe
Stil: Modern, klar, schön, nicht verschnörkelt, unesoterisch, unverspielt
Mein Logo mit Flügel: irgendwo miteinbauen
Sonstiges: anbei noch ein Iconzeichen für Kurse Seminar
Auflösung Farbe: Text & Icons für Druck (Flyer) & Webproduktpräsentation (Slideshow)
Maße: (bei 1600xca.872 px., bleiben, Banner nicht verkleinern, oder ranzoomen)

```html
<!DOCTYPE html>
<html lang="de">
<head>
<meta charset="utf-8">
<title>Engel (wieder) hören lernen – Kurse mit Annegret Holzmeier</title>
<link rel="stylesheet" href="https://fonts.googleapis.com/css2?family=Pathway+Gothic+One&family=Exo+2:ital,wght@1,300&display=swap">
<style>
  :root {
    --rose: rgba(226, 128, 124, 0.88);
    --rose-button: rgba(226, 128, 124, 0.85);
    --white: #ffffff;
    --room-wall: #efe4e3;
    --room-wall-shade: #d8c8c6;
    --room-light: #fbf7f6;
    --room-desk: #f4efed;
    --room-floor: #b89a86;
    --room-accent: #e0835a;
    --room-blush: #f0cfcd;
  }
  html, body {
    margin: 0;
    padding: 0;
    overflow: hidden;
    background: var(--room-wall);
  }
  .banner {
    position: relative;
    width: 1200px;
    height: 644px;
    overflow: hidden;
  }
  .banner__photo {
    position: absolute;
    inset: 0;
    background:
      radial-gradient(ellipse 160px 130px at 960px 500px, rgba(224,131,90,0.75) 0%, rgba(224,131,90,0) 100%),
      radial-gradient(ellipse 380px 110px at 480px 560px, var(--room-desk) 0%, rgba(244,239,237,0) 100%),
      radial-gradient(ellipse 120px 200px at 480px 370px, var(--room-blush) 0%, rgba(240,207,205,0) 100%),
      radial-gradient(ellipse 220px 200px at 950px 280px, var(--room-light) 0%, rgba(251,247,246,0) 100%),
      radial-gradient(ellipse 260px 220px at 520px 230px, var(--room-light) 0%, rgba(251,247,246,0) 100%),
      linear-gradient(90deg, var(--room-wall-shade) 0%, var(--room-wall) 30%, var(--room-wall) 75%, var(--room-wall-shade) 100%);
  }
  .banner__photo::after {
    content: "";
    position: absolute;
    left: 0; right: 0; bottom: 0;
    height: 110px;
    background: linear-gradient(180deg, rgba(184,154,134,0) 0%, var(--room-floor) 100%);
    opacity: 0.6;
  }
  .headline-circle {
    position: absolute;
    left: 22px;
    top: 19px;
    width: 390px;
    height: 390px;
    border-radius: 50%;
    background: var(--rose);
    color: var(--white);
    text-align: center;
  }
  .headline-circle__claim {
    position: absolute;
    left: 0;
    right: 0;
    top: 62px;
    margin: 0;
    font-family: "Pathway Gothic One", sans-serif;
    font-weight: 400;
    font-size: 38px;
    line-height: 38px;
    text-shadow: 1px 1px 2px rgba(0,0,0,0.35);
  }
  .headline-circle__rule {
    position: absolute;
    left: 21px;
    width: 350px;
    top: 183px;
    height: 1px;
    background: var(--white);
  }
  .headline-circle__with,
  .headline-circle__name {
    position: absolute;
    left: 0;
    right: 0;
    margin: 0;
    font-family: "Exo 2", sans-serif;
    font-style: italic;
    font-weight: 300;
    text-shadow: 2px 2px 3px rgba(0,0,0,0.4);
  }
  .headline-circle__with {
    top: 184px;
    font-size: 48px;
    line-height: 52px;
  }
  .headline-circle__name {
    top: 237px;
    font-size: 58px;
    line-height: 60px;
  }
  .more-button {
    position: absolute;
    left: 958px;
    top: 512px;
    width: 212px;
    height: 105px;
    border-radius: 42px;
    background: var(--rose-button);
    display: flex;
    align-items: center;
    justify-content: center;
    gap: 16px;
    color: var(--white);
    text-decoration: none;
  }
  .more-button__mark {
    width: 44px;
    height: 44px;
    border-radius: 50%;
    border: 2px solid var(--white);
    box-sizing: border-box;
  }
  .more-button__label {
    font-family: "Pathway Gothic One", sans-serif;
    font-size: 44px;
    line-height: 1;
    text-shadow: 1px 1px 2px rgba(0,0,0,0.3);
  }
</style>
</head>
<body>
  <div class="banner">
    <div class="banner__photo" role="img" aria-label="Foto: Frau mit blonden Locken in hellrosa Bluse sitzt schreibend an einem weißen Schreibtisch in einem hellen Raum mit Kaminsims, Herz-Bilderrahmen, Rosen, weißem Schminktisch und orangefarbener Box"></div>

    <div class="headline-circle">
      <p class="headline-circle__claim">Engel (wieder) hören<br>lernen &amp; einen<br>Seelenplan umsetzen.</p>
      <div class="headline-circle__rule"></div>
      <p class="headline-circle__with">Mit</p>
      <p class="headline-circle__name">Annegret<br>Holzmeier</p>
    </div>

    <a class="more-button" href="#">
      <span class="more-button__mark" aria-hidden="true"></span>
      <span class="more-button__label">mehr...</span>
    </a>
  </div>
</body>
</html>
```